Business Card Design

Selling beds and mattrices
See website www.lunorest.com.au for details
Targeting wholesale bed sellers

Industry/Entity Type

Business

Contact Information for Business Card

Lunorest
Director Gerald Whitcombe
Beds and Mattrices - Most technologically advanced beds in the world
European designed and made
Already No 1 seller in Europe
Call now for a quote
ph: 0472 518 306
Email: sales@lunorest.com.au
www.lunorest.com.au

```html
<!DOCTYPE html>
<html lang="en">
<head>
<meta charset="utf-8">
<title>Lunorest Business Card</title>
<link href="https://fonts.googleapis.com/css2?family=Open+Sans:wght@400;600;700&display=swap" rel="stylesheet">
<style>
:root{
  --page:#d9d6d2;
  --card-white:#f4f4f4;
  --photo-light:#e6e6e6;
  --photo-mid:#9a9a9a;
  --panel-black:#0d0d0e;
  --panel-grey:#2a2c2e;
  --panel-line:#6f7578;
  --ink:#111111;
  --white:#ffffff;
  --muted:#cfcfcf;
}
html,body{margin:0;padding:0;width:1200px;height:803px;overflow:hidden;background:var(--page);}
body{font-family:"Open Sans",Arial,sans-serif;}
.card{
  position:absolute;left:150px;top:126px;width:900px;height:550px;
  background:var(--card-white);overflow:hidden;
  box-shadow:0 10px 30px rgba(0,0,0,.25);
}
.card-photo{
  position:absolute;inset:0;
  background:
    radial-gradient(ellipse at 45% 55%, var(--photo-light) 0%, transparent 55%),
    linear-gradient(160deg, var(--card-white) 0%, var(--photo-light) 30%, var(--photo-mid) 55%, var(--photo-light) 75%, var(--card-white) 100%);
  opacity:.85;
}
.card-panel{position:absolute;inset:0;width:900px;height:550px;}
.brand-name{
  position:absolute;left:60px;top:72px;margin:0;
  font-size:58px;font-weight:400;letter-spacing:3px;color:var(--ink);line-height:1;
}
.tagline{position:absolute;left:60px;top:195px;font-size:34px;font-weight:700;color:var(--ink);margin:0;}
.pitch{position:absolute;left:60px;top:250px;font-size:24px;line-height:30px;color:var(--ink);margin:0;font-weight:600;}
.cta{position:absolute;left:60px;top:395px;margin:0;color:var(--ink);}
.cta-label{display:block;font-size:20px;font-weight:700;letter-spacing:.5px;}
.cta-phone{display:block;font-size:40px;font-weight:700;letter-spacing:1px;line-height:1.2;}
.contact{position:absolute;right:40px;top:82px;text-align:right;color:var(--white);}
.contact-name{font-size:30px;font-weight:700;margin:0;line-height:1.1;}
.contact-role{font-size:17px;letter-spacing:1px;color:var(--muted);margin:4px 0 16px;}
.contact-line{font-size:19px;margin:4px 0;display:flex;justify-content:flex-end;align-items:center;gap:10px;color:var(--muted);}
.contact-icon{width:14px;height:14px;border:1.5px solid var(--white);border-radius:50%;display:inline-block;}
</style>
</head>
<body>
<div class="card">
  <div class="card-photo" role="img" aria-label="Soft black and white photograph of a modern bed in a bright bedroom"></div>
  <svg class="card-panel" viewBox="0 0 900 550" aria-hidden="true">
    <polygon points="460,0 900,0 900,550 760,550" fill="var(--panel-black)"/>
    <polygon points="620,0 900,0 900,330" fill="var(--panel-grey)" opacity=".5"/>
    <line x1="540" y1="0" x2="900" y2="250" stroke="var(--panel-line)" stroke-width="1.5"/>
    <line x1="710" y1="0" x2="860" y2="550" stroke="var(--panel-line)" stroke-width="1" opacity=".7"/>
    <line x1="900" y1="90" x2="640" y2="550" stroke="var(--panel-line)" stroke-width="1" opacity=".5"/>
  </svg>

  <p class="brand-name">LUNOREST</p>
  <p class="tagline">Beds &amp; Mattrices</p>
  <p class="pitch">Most technologically<br>advanced beds in the world<br>European designed and made<br>Already No 1 seller in Europe</p>
  <p class="cta"><span class="cta-label">CALL NOW FOR A QUOTE ph:</span><span class="cta-phone">0472 518 306</span></p>

  <div class="contact">
    <p class="contact-name">Gerald Whitcombe</p>
    <p class="contact-role">DIRECTOR</p>
    <p class="contact-line">sales@lunorest.com.au <span class="contact-icon"></span></p>
    <p class="contact-line">www.lunorest.com.au <span class="contact-icon"></span></p>
  </div>
</div>
</body>
</html>
```